Company or website name
- Jardin Lumineux
- Slogan or Tagline
- No Taglines, but each description listed here needs to be on the front label of each of these wines.
- Describe your company and organization and target audience
- Consumers buying wine aged 30+, restaurants. Of wine buyers, 55% are female shopping at major grocery chains.
- The design should have the following
- The style should marry traditional sophistication with a touch of contemporary fun. It should tell knowledgeable wine buyers that it is a serious, quality product, but have enough light to attract the novice wine buyers and impulse buyers. Must have: 1) Jardin Lumineux (brand name) 2) Method Traditionelle 3) Appellation Cremant de Limoux Controlee 4) Product of France -Brut -Brut RoseFountaine de la Vie means "Bright Garden" in French We would like this idea implemented into the design of the label. As a sparkling wine, bubbles are what spring from this fountain.
- This design should not have this in the entries
- No use of Gold or Gold Foil (scratches too easily). Also, black labels tend to scuff and don't travel well (plus they don't stand out on the shelves as much). Not too frilly – this is a quality product. We do not want to turn off serious wine buyers because they don’t take the label seriously.

```html
<!DOCTYPE html>
<html lang="en">
<head>
<meta charset="utf-8">
<title>Jardin Lumineux – Brut label</title>
<link rel="stylesheet" href="https://fonts.googleapis.com/css2?family=Great+Vibes&family=Josefin+Sans:wght@300;400&family=Poiret+One&display=swap">
<style>
  :root {
    --page: #ffffff;
    --label: #2bbcd8;
    --pale: #c9eef6;
    --script: #8fd6e6;
    --deep: #1a8fb0;
    --ornament: #19abc9;
    --frame: #8fd8e8;
  }
  * { margin: 0; padding: 0; box-sizing: border-box; }
  html, body {
    width: 1200px;
    height: 958px;
    overflow: hidden;
    background: var(--page);
  }
  .label {
    position: absolute;
    left: 286px;
    top: 0;
    width: 626px;
    height: 958px;
    background: var(--label);
  }
  .frame-rule {
    position: absolute;
    top: 0;
    bottom: 0;
    width: 2px;
    background: var(--frame);
  }
  .frame-rule.left { left: 7px; }
  .frame-rule.right { right: 7px; }
  .style-name {
    position: absolute;
    top: 64px;
    width: 100%;
    text-align: center;
    font-family: "Josefin Sans", sans-serif;
    font-weight: 400;
    font-size: 36px;
    letter-spacing: 1px;
    color: var(--pale);
  }
  .fountain-art {
    position: absolute;
    left: 164px;
    top: 124px;
    width: 300px;
    height: 244px;
    border-radius: 48% 48% 18% 18%;
    background: radial-gradient(ellipse at 50% 60%, #1eb3d0 0%, var(--ornament) 70%, rgba(25,171,201,0) 100%);
  }
  .brand-name {
    position: absolute;
    left: 0;
    top: 400px;
    width: 100%;
    font-family: "Great Vibes", cursive;
    font-weight: 400;
    color: var(--script);
    line-height: 1;
  }
  .brand-name .line-one {
    display: block;
    padding-left: 72px;
    font-size: 104px;
  }
  .brand-name .line-two {
    display: block;
    padding-left: 220px;
    margin-top: -14px;
    font-size: 104px;
  }
  .appellation {
    position: absolute;
    top: 704px;
    width: 100%;
    text-align: center;
    font-family: "Poiret One", sans-serif;
    font-size: 31px;
    color: var(--deep);
  }
  .divider {
    position: absolute;
    left: 110px;
    top: 750px;
    width: 410px;
    height: 2px;
    background: linear-gradient(90deg, rgba(26,143,176,0) 0%, var(--deep) 30%, var(--deep) 70%, rgba(26,143,176,0) 100%);
  }
  .method {
    position: absolute;
    top: 757px;
    width: 100%;
    text-align: center;
    font-family: "Josefin Sans", sans-serif;
    font-weight: 400;
    font-size: 19px;
    letter-spacing: 2px;
    color: var(--deep);
  }
  .origin {
    position: absolute;
    top: 868px;
    width: 100%;
    text-align: center;
    font-family: "Josefin Sans", sans-serif;
    font-weight: 300;
    font-size: 20px;
    letter-spacing: 0.5px;
    color: var(--pale);
  }
</style>
</head>
<body>
  <main class="label">
    <div class="frame-rule left"></div>
    <div class="frame-rule right"></div>

    <p class="style-name">BRUT</p>

    <div class="fountain-art" role="img" aria-label="Ornamental fountain of swirling water sprays"></div>

    <h1 class="brand-name">
      <span class="line-one">Jardin</span>
      <span class="line-two">Lumineux</span>
    </h1>

    <p class="appellation">Cremant de Limoux</p>
    <div class="divider"></div>
    <p class="method">METHOD TRADITIONELLE</p>

    <p class="origin">PRODUCT OF FRANCE</p>
  </main>
</body>
</html>
```